TOTLANTERNKIT WEBSITE DESIGN

We need a website design based on the template- http://plovraskins.com/skins/ferrolpage-layout-cms-skin/. We purchased template and will build the website using wordpress. It is one page application. We wanted to list all content in one page and make it browser friendly (can be viewed in cell phone, pc, mac, ipad, etc).

The target audience is parents with babies/kids age from 0-5 year old. We wanted to sell the subscription based monthly boxes to the families. The box will include books, toys, crafts, kids consumer products and letter/note/card to the family from the experts. All boxes are customized based on children's age, gender and interests.

We wanted the site main color to be blue.

Please refer to these websites for ideas.
quorva.com
wwws.hazelpodmart.com
http://www.tiddlewrens.com/

I've updated the project brief and make the project fund guaranteed. Thanks!

Target Market(s)

Parents with kids age from 0-5 years old. Mainly target to the China market.

Industry/Entity Type

Cell Phone

Colors
3277b5
85abd2
85cae6
33a6d7
0592cd
0355a3
ceddec
cee9f5

Requirements
Must have
• Must provide the design based on the template- http://plovraskins.com/skins/ferrolpage-layout-cms-skin/.
The site has to be Chinese character friendly since we are going to post Chinese content on the website. No English content.
The registration forms needs to be designed and include in the final deliverable.

```html
<!DOCTYPE html>
<html lang="en">
<head>
<meta charset="utf-8">
<title>TOTLANTERNKIT</title>
<link rel="stylesheet" href="https://fonts.googleapis.com/css2?family=Raleway:wght@400;500;600;700;800&display=swap">
<style>
:root{
  --navy:#0355a3;
  --button:#0b4d97;
  --sky:#33a6d7;
  --light-sky:#85cae6;
  --ink:#2b2b2b;
  --muted:#444;
  --footer:#383f4c;
  --rule:#ceddec;
  --red:#e8141b;
  --white:#fff;
}
*{box-sizing:border-box;margin:0;padding:0}
html,body{width:1200px;height:2460px;overflow:hidden}
body{font-family:"Raleway",Arial,sans-serif;color:var(--ink);background:var(--white);position:relative}
.abs{position:absolute}
/* header */
.site-header{position:absolute;left:0;top:0;width:1200px;height:105px;background:var(--navy)}
.brand{position:absolute;left:92px;top:24px;display:flex;align-items:center;gap:12px;color:var(--white);font-weight:800;font-size:20px;letter-spacing:.5px}
.brand-dot{width:56px;height:56px;border-radius:50%;background:var(--white)}
.main-nav{position:absolute;right:93px;top:44px;display:flex;gap:12px;color:var(--white);font-size:10.5px;font-weight:700;text-transform:uppercase}
/* intro */
.intro{position:absolute;left:0;top:168px;width:1200px;text-align:center}
.intro-lead{font-size:18px;line-height:22px;color:#333;width:760px;margin:0 auto}
.intro-title{font-size:36px;font-weight:600;color:var(--navy);margin-top:16px}
.intro-body{font-size:12.5px;line-height:17px;color:#333;width:740px;margin:14px auto 0}
.banner{position:absolute;left:114px;top:413px;width:972px;height:258px;border:5px solid var(--navy);border-bottom:none;display:flex}
.banner div{flex:1;height:100%}
.banner .left{background:linear-gradient(135deg,#c9c6c2,#8d8a86 60%,#b8a58c)}
.banner .right{background:linear-gradient(135deg,#6b4f3a,#b77a3c 55%,#5c3b2a)}
.banner-rule{position:absolute;left:0;top:668px;width:1200px;height:5px;background:var(--navy);box-shadow:0 3px 6px rgba(0,0,0,.15)}
/* experts */
.expert{position:absolute;top:764px;width:250px;text-align:center}
.avatar{width:106px;height:106px;border-radius:50%;border:3px solid var(--light-sky);margin:0 auto;background:radial-gradient(circle at 50% 40%,#d8b8a0,#7a6a5e)}
.expert-name{font-size:15.5px;font-weight:700;margin-top:24px;color:#222;line-height:19px}
.expert-bio{font-size:10px;line-height:12.5px;color:var(--muted);width:240px;margin:6px auto 0;height:100px;overflow:hidden}
.btn{display:inline-block;background:var(--button);color:var(--white);font-size:12px;font-weight:700;padding:7px 11px;border-radius:3px}
.btn.active{background:var(--sky)}
/* products */
.products{position:absolute;left:0;top:1174px;width:1200px;height:356px;background:var(--navy)}
.tiles{position:absolute;left:35px;top:0;width:706px;height:356px;display:grid;grid-template-columns:repeat(3,1fr);grid-template-rows:repeat(2,1fr);gap:2px;background:var(--white)}
.tile{width:100%;height:100%}
.t1{background:linear-gradient(135deg,#c8cfd9,#8c9aae 60%,#d7cfc4)}
.t2{background:#2f7bc0;display:flex;flex-direction:column;align-items:center;justify-content:center;color:var(--white);font-weight:700;font-size:14px;gap:12px}
.t2 .icons{display:flex;gap:14px}
.t2 .icons svg{width:36px;height:30px}
.t3{background:linear-gradient(135deg,#e8dada,#d4b5bc 55%,#cfc6be)}
.t4{background:linear-gradient(135deg,#f3f0f4,#d9c9e0 55%,#e8d59a)}
.t5{background:linear-gradient(135deg,#b6a99b,#7a5a47 50%,#c9c2c9)}
.t6{background:linear-gradient(135deg,#f5f3f5,#e6c18a 45%,#d64a3a)}
.signup{position:absolute;left:741px;top:0;width:459px;height:356px}
.signup h2{position:absolute;left:18px;top:34px;color:var(--white);font-size:19px;font-weight:700}
.field{position:absolute;height:37px;background:var(--white);border-radius:2px;font-size:11px;color:#999;padding:12px 10px}
.field.select::after{content:"";position:absolute;right:10px;top:16px;border:5px solid transparent;border-top-color:#777}
.check{display:inline-block;width:13px;height:13px;background:var(--white);border-radius:2px;margin-left:18px;vertical-align:middle}
.subscribe{position:absolute;left:18px;top:291px;width:402px;height:43px;background:linear-gradient(#f23a3a,var(--red));border-radius:3px;color:var(--white);font-size:18px;font-weight:600;text-align:center;line-height:43px}
/* faq */
.section-title{position:absolute;font-size:16px;font-weight:600;color:#222;padding-bottom:7px;border-bottom:2px solid #333}
.faq-text{position:absolute;font-size:10.5px;line-height:14.5px;color:#333}
.faq-links{position:absolute;left:761px;top:1641px;list-style:none}
.faq-links li{font-size:10.5px;font-weight:700;color:var(--navy);height:25px}
/* blog */
.blog{position:absolute;left:0;top:1866px;width:1200px;height:295px;background:var(--sky);color:var(--white)}
.blog-head{position:absolute;left:98px;top:58px;display:flex;gap:10px;align-items:center}
.blog-head h3{font-size:15px;font-weight:700}
.blog-head p{font-size:12px}
.blog-rule{position:absolute;left:98px;top:112px;width:1004px;height:2px;background:var(--white)}
.blog-col{position:absolute;top:125px;list-style:none}
.blog-col li{font-size:12.5px;font-weight:700;height:23px}
.blog-col li small{font-weight:400;font-size:12px;opacity:.95}
/* footer */
.site-footer{position:absolute;left:0;top:2161px;width:1200px;height:299px;background:var(--footer);color:var(--white)}
.foot-col{position:absolute;top:62px;width:318px}
.foot-col h4{font-size:15px;font-weight:700;padding-bottom:8px;border-bottom:2px solid var(--white)}
.foot-menu{font-size:10px;font-weight:700;text-transform:uppercase;line-height:20px;margin-top:10px}
.foot-menu .on{color:var(--light-sky)}
.socials{display:flex;gap:11px;margin-top:14px}
.socials span{width:42px;height:42px;border-radius:50%;border:2px solid #6b7385;background:#4a5263}
.socials span.on{background:var(--sky);border-color:var(--white)}
.contact{font-size:13px;line-height:21px;margin-top:10px}
.contact b{font-weight:700;color:#d8dde6}
</style>
</head>
<body>

<header class="site-header">
  <div class="brand"><span class="brand-dot"></span>TOTLANTERNKIT</div>
  <nav class="main-nav">
    <span>Order now</span><span>|</span>
    <span>About us</span><span>|</span>
    <span>Our experts</span><span>|</span>
    <span>FAQ</span><span>|</span>
    <span>Share</span><span>|</span>
    <span>ChatLine &#9662;</span>
  </nav>
</header>

<section class="intro">
  <p class="intro-lead">U.S. baby book club - let the children stay at home and enjoy the best the United States early education and childcare philosophy platform.</p>
  <h1 class="intro-title">Subscribe now to our monthly mysterious parcel,</h1>
  <p class="intro-body">father and mother and baby can get U.S. experts recommend the award-winning children's books and American original reading experience, cultivate good habits of children daily necessities, as well as the latest toys handmade infant intellectual development. Mom and Dad will gain double surprise.<br>Authoritative parenting expert with the United States to exchange one pair of one, with the scientific, personalized parenting philosophy. Books and articles to help your baby healthy and happy growth.</p>
</section>

<div class="banner">
  <div class="left" role="img" aria-label="Open gift box with a plush bear, crayons and a book"></div>
  <div class="right" role="img" aria-label="Open gift box with picture books and toddler toys"></div>
</div>
<div class="banner-rule"></div>

<section class="experts">
  <div class="expert" style="left:68px">
    <div class="avatar" role="img" aria-label="Portrait of pediatrician expert"></div>
    <h3 class="expert-name">Wen Haoran, MD, double</h3>
    <p class="expert-bio">Bayfield General Hospital pediatrician and physician Assistant clinical professor of pediatrics at Corliss Medical School National Pediatric Council Senior Member Regional Pediatric Gastroenterology, Hepatology and Nutrition Institute (Pediatric Gut Society) Member</p>
    <span class="btn">More info</span>
  </div>
  <div class="expert" style="left:332px">
    <div class="avatar" role="img" aria-label="Portrait of pediatric dentist expert"></div>
    <h3 class="expert-name">Dr. Neil R. Ashby</h3>
    <p class="expert-bio">A member of the Pediatric Dental Circle Pediatric Dentistry Association State Dental Association members Regional Dental Society members Eastbrook Institute of Child Dentistry, former president</p>
    <span class="btn active">More info</span>
  </div>
  <div class="expert" style="left:618px">
    <div class="avatar" role="img" aria-label="Portrait of reading education expert"></div>
    <h3 class="expert-name">Doreen Halvick</h3>
    <p class="expert-bio">American reading education experts Bachelor's degree from Ridgemoor University American English Master of Education, Lakemont Crest University U.S. renowned reading specialist certification</p>
    <span class="btn">More info</span>
  </div>
  <div class="expert" style="left:885px">
    <div class="avatar" role="img" aria-label="Portrait of early childhood teacher"></div>
    <h3 class="expert-name">Fang Mei early childhood</h3>
    <p class="expert-bio">New York, Thornvale Crest University Graduate School of Education Boston private school teacher</p>
    <span class="btn">More info</span>
  </div>
</section>

<section class="products">
  <div class="tiles">
    <div class="tile t1" role="img" aria-label="Gift box with blue plush bear and crayons"></div>
    <div class="tile t2">
      <span>PRODUCT NO: 2</span>
      <div class="icons">
        <svg viewBox="0 0 36 30"><rect x="1" y="1" width="34" height="28" rx="2" fill="none" stroke="#fff" stroke-width="1.5"/><circle cx="17" cy="14" r="4.5" fill="none" stroke="#fff" stroke-width="1.8"/><line x1="20.5" y1="17.5" x2="24" y2="21" stroke="#fff" stroke-width="2"/></svg>
        <svg viewBox="0 0 36 30"><rect x="1" y="1" width="34" height="28" rx="2" fill="none" stroke="#fff" stroke-width="1.5"/><rect x="11" y="13" width="9" height="5" rx="2.5" transform="rotate(-45 15.5 15.5)" fill="none" stroke="#fff" stroke-width="1.8"/><rect x="16" y="12" width="9" height="5" rx="2.5" transform="rotate(-45 20.5 14.5)" fill="none" stroke="#fff" stroke-width="1.8"/></svg>
      </div>
    </div>
    <div class="tile t3" role="img" aria-label="Gift box with pink plush bear"></div>
    <div class="tile t4" role="img" aria-label="Wooden toy train with animals"></div>
    <div class="tile t5" role="img" aria-label="Plush monkey backpack and bear in a box"></div>
    <div class="tile t6" role="img" aria-label="Wooden bead maze activity truck"></div>
  </div>
  <form class="signup">
    <h2>SUBSCRIBE FOR MYSTERIOUS PARCEL</h2>
    <div class="field" style="left:18px;top:68px;width:199px">Child's Name</div>
    <div class="field select" style="left:222px;top:68px;width:198px">Gender</div>
    <div class="field" style="left:18px;top:112px;width:199px">Birth date (dd\mm\yy)</div>
    <div class="field" style="left:222px;top:112px;width:198px">Your email</div>
    <div class="field" style="left:18px;top:156px;width:402px">Mailing address</div>
    <div class="field" style="left:18px;top:202px;width:402px">Phone</div>
    <div class="abs" style="left:18px;top:259px;color:#fff;font-size:11px;font-weight:700">Select the subscription plan :<span class="check"></span>&nbsp; 6 months<span class="check" style="margin-left:34px"></span>&nbsp; 1 year</div>
    <div class="subscribe">Subscribe now</div>
  </form>
</section>

<section class="faq">
  <h2 class="section-title" style="left:84px;top:1594px;width:656px">Frequently Asked Questions</h2>
  <p class="faq-text" style="left:84px;top:1641px;width:306px">We are parenting experts from the United States in New England, doctors, teachers and college professors, is a group dedicated to creating a better future moms and dads for children. In the daily work and life, we often see a lot of parents in the face of the child-related issues at a loss, and into errors in the direction of their children's education and methods. We voluntarily initiated TOTLANTERNKIT, hope that through our many years of expertise and experience to provide you with school-age children the best educational programs as well as medical advice.</p>
  <p class="faq-text" style="left:404px;top:1641px;width:334px">TOTLANTERNKIT headquartered in Boston, this one of America's oldest, most historic and cultural value of the city. It is not only the New England economy and the cultural center, where the United States also has the best educational environment. Now, let your baby and American children to come and experience New England School of gas, to meet the future and lay a solid foundation. Help you bring hope to the most promising future baby.</p>
  <span class="btn abs" style="left:404px;top:1764px;background:#3a3f47">More info</span>
  <h2 class="section-title" style="left:761px;top:1594px;width:294px">About Us</h2>
  <ul class="faq-links">
    <li>· What TOTLANTERNKIT is?</li>
    <li>· How to join TOTLANTERNKIT?</li>
    <li>· When will I receive my first one mysterious parcel?</li>
    <li>· Do I need to pay for shipping it?</li>
    <li>· I can send TOTLANTERNKIT mysterious parcel to my friend?</li>
    <li>· About unsubscribe, you have what provisions?</li>
    <li>· What is your return policy is how to provide?</li>
  </ul>
</section>

<section class="blog">
  <div class="blog-head">
    <svg width="64" height="44" viewBox="0 0 64 44"><path d="M4 4h34a4 4 0 0 1 4 4v14a4 4 0 0 1-4 4H18l-9 8v-8H4a4 4 0 0 1-4-4V8a4 4 0 0 1 4-4z" fill="#fff"/><path d="M46 12h12a4 4 0 0 1 4 4v12a4 4 0 0 1-4 4h-2v7l-8-7H30a4 4 0 0 1-4-4h14a6 6 0 0 0 6-6z" fill="#fff" opacity=".85"/></svg>
    <div><h3>BLOG POSTS</h3><p>Latest posts</p></div>
  </div>
  <div class="blog-rule"></div>
  <ul class="blog-col" style="left:98px"><li>• Lorem ipsum dolor <small>(21-12-14)</small></li><li>• Ipsum dolor sit ampet <small>(20-12-14)</small></li><li>• Lorem ipsum dolor <small>(22-12-14)</small></li></ul>
  <ul class="blog-col" style="left:362px"><li>• Lorem ipsum dolor <small>(21-12-14)</small></li><li>• Ipsum dolor sit ampet <small>(20-12-14)</small></li><li>• Lorem ipsum dolor <small>(22-12-14)</small></li></ul>
  <ul class="blog-col" style="left:626px"><li>• Lorem ipsum dolor <small>(21-12-14)</small></li><li>• Ipsum dolor sit ampet <small>(20-12-14)</small></li><li>• Lorem ipsum dolor <small>(22-12-14)</small></li></ul>
  <ul class="blog-col" style="left:891px"><li>• Lorem ipsum dolor <small>(21-12-14)</small></li><li>• Ipsum dolor sit ampet <small>(20-12-14)</small></li><li>• Lorem ipsum dolor <small>(22-12-14)</small></li></ul>
</section>

<footer class="site-footer">
  <div class="foot-col" style="left:98px">
    <h4>MENU</h4>
    <div class="foot-menu"><span class="on">Home</span> &nbsp;| &nbsp;Order now &nbsp;| &nbsp;About us &nbsp;| &nbsp;Our experts<br>FAQ &nbsp;| &nbsp;Share &nbsp;| &nbsp;Sitemap &nbsp;| &nbsp;Privacy policy</div>
  </div>
  <div class="foot-col" style="left:441px">
    <h4>Social Media</h4>
    <div class="socials"><span></span><span class="on"></span><span></span><span></span><span></span><span></span></div>
  </div>
  <div class="foot-col" style="left:784px">
    <h4>Contact Us</h4>
    <div class="contact">Elm Row, 412, 10550, Harbor City,<br>United States.<br><b>Tlf.: +(100) 55 01 23 45 67</b><br><b>Mail: info@totlanternkit.com</b></div>
  </div>
</footer>

</body>
</html>
```